DELLOWAY 'S TRUE GOLDEN NUT SPREAD Co. In need of some labels!

We need a label for a new product line. We are going to eventually need several different labels made for different types of products. As for now we are looking only for 3 product labels.

They will be:
1. Delloway's True Golden Nut Spread Creamy
2. Delloway's True Golden Nut Spread Crunchy
3. Delloway's True Golden Nut Spread Sweet

As far as colors something bright and catchy. Otherwise leaving it in the hands of the designers.

Target Market(s)

Health and fitness

Industry/Entity Type

Product

Font styles to use
Decorative
Script

Requirements
Must have
• Would like Delloway's True golden Nut spread. To stand out. So it will be easily seen on the store shelves.

```html
<!DOCTYPE html>
<html lang="en">
<head>
<meta charset="utf-8">
<title>Delloway's True Golden Nut Spread – Creamy Label</title>
<link rel="stylesheet" href="https://fonts.googleapis.com/css2?family=Fredericka+the+Great&family=Tinos:ital,wght@1,400&display=swap">
<style>
  :root {
    --red-deep: #7e0000;
    --red-mid: #b80004;
    --red-bright: #e60a0a;
    --ink-white: #ffffff;
    --band-green: #62dd0a;
    --band-light: #8cf21c;
    --band-edge: #d8ff4a;
    --badge-orange: #ff7a00;
    --badge-yellow: #fff200;
    --badge-text: #e3101c;
  }
  html, body {
    margin: 0;
    padding: 0;
    overflow: hidden;
    background: var(--red-mid);
  }
  .label {
    position: relative;
    width: 1200px;
    height: 857px;
    overflow: hidden;
  }
  .label__backdrop {
    position: absolute;
    inset: 0;
    background:
      radial-gradient(ellipse 70% 60% at 75% 35%, var(--red-bright) 0%, rgba(230,10,10,0) 70%),
      linear-gradient(120deg, var(--red-deep) 0%, var(--red-mid) 45%, var(--red-bright) 80%, var(--red-mid) 100%);
  }
  .label__layer {
    position: absolute;
    inset: 0;
  }
  .brand-line {
    font-family: "Fredericka the Great", cursive;
    font-size: 96px;
    fill: var(--ink-white);
  }
  .band-title {
    font-family: "Fredericka the Great", cursive;
    font-size: 68px;
    fill: url(#gold-ink);
    stroke: #5a7a00;
    stroke-width: 1;
  }
  .variety-badge {
    position: absolute;
    left: 413px;
    top: 600px;
    width: 370px;
    height: 118px;
    border-radius: 18px;
    background: linear-gradient(180deg, var(--badge-orange) 0%, var(--badge-yellow) 45%, var(--badge-yellow) 60%, var(--badge-orange) 100%);
    display: flex;
    align-items: center;
    justify-content: center;
  }
  .variety-badge__name {
    margin: 0;
    font-family: "Tinos", "Times New Roman", serif;
    font-style: italic;
    font-size: 78px;
    letter-spacing: 5px;
    color: var(--badge-text);
  }
</style>
</head>
<body>
<main class="label">
  <div class="label__backdrop" role="img" aria-label="Red background with glowing sparkles and flowing light lines"></div>

  <svg class="label__layer" width="1200" height="857" viewBox="0 0 1200 857" role="img" aria-label="Curled green ribbon banner">
    <defs>
      <linearGradient id="band-fill" x1="0" y1="0" x2="0" y2="1">
        <stop offset="0" stop-color="var(--band-light)"/>
        <stop offset="1" stop-color="var(--band-green)"/>
      </linearGradient>
    </defs>
    <polygon class="title-band" points="250,305 890,420 875,560 232,445" fill="url(#band-fill)" stroke="var(--band-edge)" stroke-width="4"/>
  </svg>

  <svg class="label__layer" width="1200" height="857" viewBox="0 0 1200 857">
    <defs>
      <linearGradient id="gold-ink" x1="0" y1="0" x2="0" y2="1">
        <stop offset="0" stop-color="#ffe81a"/>
        <stop offset="1" stop-color="#ff7a00"/>
      </linearGradient>
    </defs>
    <text class="brand-line" transform="translate(30 170) rotate(13)" textLength="1150" lengthAdjust="spacingAndGlyphs">Delloway's true golden</text>
    <text class="band-title" transform="translate(280 372) rotate(13)" textLength="500" lengthAdjust="spacingAndGlyphs">Nut spread</text>
  </svg>

  <div class="variety-badge">
    <p class="variety-badge__name">Creamy</p>
  </div>
</main>
</body>
</html>
```